Veltrano Equity Partners business cards

Our company name is VELTRANO EQUITY PARTNERS. We need a business card for a start up company located in Medellin Colombia. The company will also be shortly expanding to USA. We are a Biotech company responsible for funding regenerative medicine projects with an emphasis on stem cell treatment and regeneration clinics. This will be a global company so the final design should communicate world wide financing for the new generation of regenerative medicine.

Industry/Entity Type

Business

```html
<!DOCTYPE html>
<html lang="en">
<head>
<meta charset="utf-8">
<title>Veltrano Equity Partners – Business Card</title>
<link href="https://fonts.googleapis.com/css2?family=Jost:wght@300;400;500&display=swap" rel="stylesheet">
<style>
  :root {
    --page-bg: #e9e3ea;
    --card-purple: #7d0a72;
    --card-purple-deep: #6a0862;
    --helix-light: rgba(194, 60, 180, 0.85);
    --helix-mid: rgba(160, 31, 149, 0.45);
    --helix-fade: rgba(125, 10, 114, 0);
    --text-white: #ffffff;
    --text-soft: #f3dff0;
  }
  * { margin: 0; padding: 0; box-sizing: border-box; }
  html, body {
    width: 1200px;
    height: 1000px;
    overflow: hidden;
    background: var(--page-bg);
    font-family: "Jost", "Futura", sans-serif;
  }
  .canvas {
    width: 1200px;
    height: 1000px;
    display: flex;
    align-items: center;
    justify-content: center;
  }
  .business-card {
    position: relative;
    width: 840px;
    height: 480px;
    background: linear-gradient(160deg, var(--card-purple) 0%, var(--card-purple-deep) 100%);
    overflow: hidden;
    box-shadow: 0 18px 40px rgba(60, 10, 55, 0.25);
  }
  .helix-decoration {
    position: absolute;
    inset: 0;
    background: radial-gradient(ellipse 380px 300px at 10% 8%,
      var(--helix-light) 0%,
      var(--helix-mid) 45%,
      var(--helix-fade) 100%);
  }
  .company-name {
    position: absolute;
    right: 60px;
    top: 110px;
    text-align: right;
    color: var(--text-white);
    font-weight: 400;
    line-height: 1.1;
  }
  .company-name .name-main {
    display: block;
    font-size: 40px;
    letter-spacing: 2px;
  }
  .company-name .name-sub {
    display: block;
    font-size: 22px;
    letter-spacing: 1px;
  }
  .person {
    position: absolute;
    left: 420px;
    top: 232px;
    width: 220px;
    color: var(--text-white);
    font-weight: 300;
    text-align: center;
    line-height: 1.35;
  }
  .person-name { font-size: 24px; }
  .person-title { font-size: 20px; }
  .contact-list {
    position: absolute;
    left: 380px;
    top: 320px;
    list-style: none;
    color: var(--text-soft);
    font-weight: 300;
    font-size: 18px;
    line-height: 1.45;
  }
  .contact-list .label {
    display: inline-block;
    width: 22px;
  }
</style>
</head>
<body>
  <main class="canvas">
    <section class="business-card">
      <div class="helix-decoration" role="img" aria-label="Soft DNA helix decoration in magenta tones"></div>

      <div class="company-name">
        <span class="name-main">VELTRANO</span>
        <span class="name-sub">Equity Partners</span>
      </div>

      <div class="person">
        <p class="person-name">Lucía Marín</p>
        <p class="person-title">CEO &amp; Founder</p>
      </div>

      <ul class="contact-list">
        <li><span class="label">m</span>+44 (0)20 7946 0321</li>
        <li><span class="label">t</span>+44 (0)20 7946 0321</li>
        <li><span class="label">e</span>l.marin@veltrano.eu</li>
        <li><span class="label">w</span>www.veltrano-equity.com</li>
      </ul>
    </section>
  </main>
</body>
</html>
```